Australian Civil Construction, Quarry & Mining Services needs a business card

We need a business card designed for our Civil Construction, Quarry & Mining Services based in the country in Australia.
Our Company Brackley Earthworks provide innovate solutions for infrastructure, agricultural and mining (aggregate, sand, roadbase) industry.
We would like our business cards to be double sided
Front of card: black background or something that resembles our business colours. (it doesn't have to be black we are open to options)
- Company name - Brackley Earthworks
- Either our logo or some sort of icon/picture that resembles our business
- Website - https://brackleyearthworks.com.au/
- We will have a number of different names, positions descriptions, phone numbers and emails on separate cards for each of our managers/directors

```html
<!DOCTYPE html>
<html lang="en">
<head>
<meta charset="utf-8">
<title>Brackley Earthworks – Business Card</title>
<link rel="stylesheet" href="https://fonts.googleapis.com/css2?family=Arimo:wght@400;700&display=swap">
<style>
  :root {
    --backdrop: #e6e5e2;
    --card: #2c2c2e;
    --card-deep: #242426;
    --orange: #f07c1a;
    --edge: #c8620f;
    --text: #f2f2f2;
    --rule: #d9d9d9;
    --emboss: #3b3b3e;
  }
  * { margin: 0; padding: 0; box-sizing: border-box; }
  html, body {
    width: 1200px; height: 801px; overflow: hidden;
    background: var(--backdrop);
    font-family: "Arimo", Arial, sans-serif;
  }
  .sheet {
    position: relative; width: 1200px; height: 801px;
    display: flex; align-items: center; justify-content: center; gap: 24px;
  }
  .card {
    position: relative; width: 540px; height: 309px;
    background: var(--card);
    border-bottom: 4px solid var(--edge);
    box-shadow: 0 10px 24px rgba(0,0,0,0.22);
    overflow: hidden;
  }
  /* front */
  .card-front { display: flex; align-items: center; }
  .brand-block {
    width: 250px; display: flex; align-items: center; justify-content: center; gap: 10px;
  }
  .brand-mark { width: 16px; height: 16px; background: var(--orange); flex: none; }
  .brand-name {
    color: var(--orange); font-weight: 700; font-size: 21px; line-height: 1.1;
    text-transform: uppercase; letter-spacing: 0.5px;
  }
  .divider { width: 1px; height: 150px; background: var(--rule); flex: none; }
  .contact-block { padding-left: 26px; color: var(--text); }
  .person-name {
    color: var(--orange); font-size: 21px; font-weight: 400; letter-spacing: 0.5px;
    text-transform: uppercase;
  }
  .person-role { font-size: 14px; margin-top: 3px; }
  .address { font-size: 13px; line-height: 1.35; margin-top: 14px; }
  .contact-list { list-style: none; margin-top: 12px; font-size: 13px; }
  .contact-list li { display: flex; align-items: center; gap: 8px; line-height: 1.55; }
  .contact-icon { width: 12px; height: 12px; flex: none; }
  /* back */
  .card-back {
    background: linear-gradient(135deg, var(--card-deep), var(--card) 60%);
    display: flex; align-items: center; justify-content: center; gap: 16px;
  }
  .card-back .brand-mark { width: 28px; height: 28px; }
  .card-back .brand-name { font-size: 36px; letter-spacing: 1px; }
</style>
</head>
<body>
<main class="sheet">
  <section class="card card-front" aria-label="Business card front">
    <div class="brand-block">
      <span class="brand-mark" aria-hidden="true"></span>
      <span class="brand-name">Brackley<br>Earthworks</span>
    </div>
    <div class="divider" aria-hidden="true"></div>
    <div class="contact-block">
      <h1 class="person-name">Daniel Hartley</h1>
      <p class="person-role">Manager</p>
      <p class="address">27 Redgum Road<br>Tallarook Victoria 3659, Australia</p>
      <ul class="contact-list">
        <li>
          <svg class="contact-icon" viewBox="0 0 24 24" aria-hidden="true"><path fill="var(--orange)" d="M6.6 10.8a15.1 15.1 0 0 0 6.6 6.6l2.2-2.2c.3-.3.7-.4 1-.2 1.1.4 2.3.6 3.6.6.6 0 1 .4 1 1V20c0 .6-.4 1-1 1A17 17 0 0 1 3 4c0-.6.4-1 1-1h3.5c.6 0 1 .4 1 1 0 1.3.2 2.5.6 3.6.1.3 0 .7-.2 1z"/></svg>
          03 5912 8046
        </li>
        <li>
          <svg class="contact-icon" viewBox="0 0 24 24" aria-hidden="true"><rect x="2" y="5" width="20" height="14" fill="var(--orange)"/><path d="M2 5l10 8 10-8" fill="none" stroke="var(--card)" stroke-width="2"/></svg>
          admin@brackleyearthworks.com.au
        </li>
        <li>
          <svg class="contact-icon" viewBox="0 0 24 24" aria-hidden="true"><circle cx="12" cy="12" r="10" fill="var(--orange)"/><path d="M2 12h20M12 2c3 3 3 17 0 20M12 2c-3 3-3 17 0 20" fill="none" stroke="var(--card)" stroke-width="1.6"/></svg>
          www.brackleyearthworks.com.au
        </li>
      </ul>
    </div>
  </section>

  <section class="card card-back" aria-label="Business card back">
    <span class="brand-mark" aria-hidden="true"></span>
    <span class="brand-name">Brackley<br>Earthworks</span>
  </section>
</main>
</body>
</html>
```